Company Brochure / Sales Sheet

We would like a brochure that we will may print out as well as forward electronically to our prospective clients.

Our clients are inventors/doctors/surgeons of medical products who need help completing their medical product, gaining approval, and then selling their product into the US market

Target Market(s)

Inventors of medical products who want to sell them in the United States

Industry/Entity Type

Medical

Font styles to use
Serif
Sans Serif

Requirements
Must have
• The word "Medical" should not receive special empahsis.
• Use the last two photos and whatever other photos that look good. You can edit and crop the photos
• Text should be easy to read
Nice to have
• We want to show that we have a lot of products.
• Sharp, clean, modern
• Minimum two pages - final product should be capable of being printed and
• forwarded electronically
• Easy to read
Should not have
• Should not be cluttered

```html
<!DOCTYPE html>
<html lang="en">
<head>
<meta charset="utf-8">
<title>Clinical Bridge Partners – Brochure</title>
<link href="https://fonts.googleapis.com/css2?family=Montserrat:wght@600;700&family=Open+Sans:wght@400;600&family=Crimson+Text:ital@1&display=swap" rel="stylesheet">
<style>
:root{
  --red:#a51c30;
  --ink:#222;
  --text:#3a3a3a;
  --grey-bar:#7d7d80;
  --panel:#ececec;
  --bg:#d9d9db;
  --navy:#2c2f78;
  --violet:#6a5fb5;
  --photo-blue:#5b8fd0;
}
*{box-sizing:border-box;margin:0;padding:0}
html,body{width:1200px;height:1200px;overflow:hidden}
body{background:var(--bg);font-family:"Open Sans",sans-serif;color:var(--text);position:relative}
.page{position:absolute;top:230px;width:570px;height:737px;background:#fff;box-shadow:0 10px 30px rgba(0,0,0,.25);overflow:hidden}
.page--about{left:15px}
.page--catalogue{left:615px}

/* header */
.pattern{position:absolute;background:linear-gradient(160deg,var(--violet) 0%,var(--navy) 45%,#1b1d55 70%,var(--violet) 100%)}
.band{position:absolute;height:10px;background:var(--red)}
.tagline{position:absolute;height:10px;font-family:"Crimson Text",serif;font-style:italic;font-size:10px;line-height:10px;color:#fff}
.brand{position:absolute;top:0;width:188px;height:107px;background:#fff;display:flex;flex-direction:column;align-items:center;justify-content:center;padding-top:14px}
.brand__mark{width:34px;height:34px;border-radius:50%;background:var(--red);margin-bottom:8px}
.brand__name{font-family:"Montserrat",sans-serif;font-weight:700;font-size:12.5px;color:var(--ink);text-align:center;line-height:1.25;letter-spacing:.2px}
.brand__name span{display:block;font-size:9px;letter-spacing:4px}

/* about page */
.heading-black{position:absolute;left:34px;width:501px;top:126px;height:24px;background:#000;color:#fff;font-family:"Montserrat",sans-serif;font-weight:700;font-size:17px;line-height:24px;padding-left:9px}
.about-copy{position:absolute;left:34px;width:505px;top:156px;font-size:9.2px;line-height:13px}
.about-copy p{margin-bottom:4px}
.heading-grey{background:var(--grey-bar);color:#fff;font-family:"Montserrat",sans-serif;font-weight:700;font-size:12.5px;letter-spacing:-.2px;height:20px;line-height:20px;padding-left:5px;white-space:nowrap}
.col{position:absolute;top:375px;width:246px;font-size:9.2px;line-height:14px}
.col p{margin-top:8px}
.col--left{left:34px}
.col--right{left:290px}
.photo{position:absolute;background:linear-gradient(135deg,#8fb4e6 0%,var(--photo-blue) 50%,#2e5ea8 100%)}
.about-photo{left:34px;top:540px;width:246px;height:150px}
.regulatory{position:absolute;left:290px;top:522px;width:245px;height:168px;background:var(--panel);padding:9px 13px;font-size:9.2px;line-height:14px}
.regulatory .heading-grey{margin-bottom:16px}

.footer{position:absolute;left:0;right:0;bottom:0;height:34px;background:var(--red);display:flex;justify-content:space-between;align-items:center;padding:0 34px;color:#fff;font-family:"Montserrat",sans-serif;font-weight:600;font-size:10.5px;letter-spacing:.6px}
.footer-rule{position:absolute;left:0;right:0;bottom:38px;height:3px;background:var(--red)}

/* catalogue page */
.tile{position:absolute;border:1px solid #9a9a9a;background:linear-gradient(160deg,#fafafa 0%,#d8d8d8 100%)}
.caption{position:absolute;background:var(--red);color:#fff;font-size:7.5px;line-height:10px;padding-left:4px}
.tile--blue{background:linear-gradient(135deg,#5aa0e0,#123a8a)}
.tile--fabric{background:linear-gradient(135deg,#6d8fc4,#3e5e98)}
</style>
</head>
<body>

<section class="page page--about">
  <div class="pattern" style="left:0;top:0;width:25px;height:97px"></div>
  <div class="pattern" role="img" aria-label="Abstract blue mesh texture" style="left:213px;top:0;width:357px;height:97px"></div>
  <div class="band" style="left:0;top:97px;width:25px"></div>
  <div class="band" style="left:213px;top:97px;width:357px"></div>
  <div class="tagline" style="left:213px;top:97px;width:345px;text-align:right">Saving Lives &amp; Reducing Health Care Costs</div>
  <div class="brand" style="left:25px">
    <div class="brand__mark"></div>
    <div class="brand__name">CLINICAL BRIDGE<span>PARTNERS</span></div>
  </div>

  <h1 class="heading-black">About Us</h1>
  <div class="about-copy">
    <p>We are a network of medical distribution professionals including physicians and surgeons, regulatory and coding experts, patent and trademark lawyers, international fulfillment experts, marketing and advertising professionals, and business strategists all working together in the distribution of promising new medical products. We handle all aspects of new surgical product sales, marketing, and distribution.</p>
    <p>Our company was founded in Harbor Point, Delaware, with distribution locations and support associates and affiliates located throughout the US. We have extensive experience with medical product development, intellectual property, and regulatory and compliances issues.</p>
    <p>We partner with medical innovators by providing strategic support with intellectual property and regulatory approval, reimbursement coding, marketing, selling and distributing state of the art medical products. Our clients include highly creative medical companies with strong management teams and consumer-driven growth perspectives.</p>
    <p>Our products are uniquely positioned in an evolving health sector to offer benefits to patients, healthcare institutions, medical professionals, insurance companies and governmental agencies. Our evidence-based technologies reduce overall healthcare expenses and empower physicians and surgeons to provide improved practices and standards of care.</p>
  </div>

  <div class="col col--left">
    <h2 class="heading-grey">Medical Products</h2>
    <p>We specialize in the distribution of next generation medical products including customized surgical instruments and kits, monitoring and diagnostic devices, advanced wound care products and innovative acute care disposables</p>
    <p style="margin-top:4px">Our medical products represent breakthroughs in medical technology, saving lives, reducing health care costs, improving patient lifestyles.</p>
  </div>
  <div class="col col--right">
    <h2 class="heading-grey">Intellectual Property &amp; Branding</h2>
    <p>We help our partners get the trademarks and patent claim approvals they need and deserve and at a reasonable price. Our team of patent attorneys and agents is effective and affordable and has gained over 300 client patent approvals. We help our clients brand and position their products for successful product launches and introductions to the US market.</p>
  </div>

  <div class="photo about-photo" role="img" aria-label="Surgical team at work in an operating room, tinted blue"></div>
  <div class="regulatory">
    <h2 class="heading-grey">Regulatory Issues</h2>
    <p>We provide comprehensive services support for global physician inventors who are seeking to distribute their medical products within the United States. We assist in navigating the unique aspects of the US medical market -- including FDA compliance and device returns, US Customs, and reimbursement coding.</p>
  </div>

  <div class="footer-rule"></div>
  <footer class="footer"><span>(555) 014-2290</span><span>www.clinicalbridgepartners.com</span></footer>
</section>

<section class="page page--catalogue">
  <div class="pattern" role="img" aria-label="Abstract blue mesh texture" style="left:0;top:0;width:357px;height:97px"></div>
  <div class="pattern" style="left:545px;top:0;width:25px;height:97px"></div>
  <div class="band" style="left:0;top:97px;width:357px"></div>
  <div class="band" style="left:545px;top:97px;width:25px"></div>
  <div class="tagline" style="left:12px;top:97px;width:340px">Saving Lives &amp; Reducing Health Care Costs</div>
  <div class="brand" style="left:357px">
    <div class="brand__mark"></div>
    <div class="brand__name">CLINICAL BRIDGE<span>PARTNERS</span></div>
  </div>

  <div class="tile" role="img" aria-label="Surgical clamp" style="left:33px;top:128px;width:118px;height:116px"></div>
  <div class="caption" style="left:33px;top:244px;width:118px">Clamps</div>
  <div class="tile" role="img" aria-label="Minimally invasive grasper" style="left:162px;top:128px;width:118px;height:116px"></div>
  <div class="caption" style="left:162px;top:244px;width:118px">Minimally Invasive</div>
  <div class="tile" role="img" aria-label="Blue-handled forceps" style="left:290px;top:128px;width:118px;height:116px"></div>
  <div class="caption" style="left:290px;top:244px;width:118px">Forceps</div>
  <div class="tile" role="img" aria-label="Surgical scissors" style="left:419px;top:128px;width:117px;height:116px"></div>
  <div class="caption" style="left:419px;top:244px;width:117px">Scissors</div>

  <div class="tile tile--fabric" role="img" aria-label="Incision wound dressing on blue cloth" style="left:33px;top:268px;width:247px;height:115px"></div>
  <div class="caption" style="left:33px;top:383px;width:247px">Subcutaneous, closed incision wound dressing</div>
  <div class="tile tile--blue" role="img" aria-label="Yellow cob elevator and suction device" style="left:290px;top:268px;width:118px;height:115px"></div>
  <div class="caption" style="left:290px;top:383px;width:118px;line-height:9.5px;height:20px">Combination cob elevator and suction device</div>
  <div class="tile" role="img" aria-label="Orthopedic cutter" style="left:419px;top:268px;width:117px;height:115px"></div>
  <div class="caption" style="left:419px;top:383px;width:117px">Orthopedic</div>

  <div class="tile" role="img" aria-label="Rongeur" style="left:34px;top:414px;width:78px;height:76px"></div>
  <div class="tile" role="img" aria-label="Rongeur" style="left:119px;top:414px;width:76px;height:76px"></div>
  <div class="tile" role="img" aria-label="Rongeur" style="left:204px;top:414px;width:76px;height:76px"></div>
  <div class="tile" role="img" aria-label="Dissector" style="left:34px;top:499px;width:78px;height:77px"></div>
  <div class="tile" role="img" aria-label="Probe" style="left:119px;top:499px;width:76px;height:77px"></div>
  <div class="tile" role="img" aria-label="Retractor" style="left:204px;top:499px;width:76px;height:77px"></div>
  <div class="tile" role="img" aria-label="Bone cutter" style="left:34px;top:586px;width:78px;height:76px"></div>
  <div class="tile" role="img" aria-label="Surgical mallet" style="left:119px;top:586px;width:76px;height:76px"></div>
  <div class="tile" role="img" aria-label="Needle driver" style="left:204px;top:586px;width:76px;height:76px"></div>
  <div class="tile" role="img" aria-label="Needle holder close-up" style="left:289px;top:414px;width:117px;height:117px"></div>
  <div class="photo" role="img" aria-label="Surgical team at work in an operating room, tinted blue" style="left:289px;top:537px;width:246px;height:125px"></div>

  <div class="footer-rule"></div>
  <footer class="footer"><span>www.clinicalbridgepartners.com</span><span>(555) 014-2290</span></footer>
</section>

</body>
</html>
```